Refresh our Logo and Letterhead!

We would like to see designs with blue, green, teal etc. Our current logo and contact details for the letterhead is attached.
We're a small boutique firm based in Sydney, Australia. We're near the coast and not opposed to coastal images. We practice in property law and have primarily female practitioners, although we don't necessarily need the logo and letterhead to be too feminine. We would like to see designs with blue, green, teal etc. Our current logo and contact details for the letterhead is attached.
We're a small boutique firm based in Sydney, Australia. We're near the coast and not opposed to coastal images. We practice in property law and have primarily female practitioners, although we don't necessarily need the logo and letterhead to be too feminine.

Target Market(s)

Young professionals

Industry/Entity Type

Law Firm

Logo Text

Marwick Legal

Font styles to use
Serif
Sans Serif

Colors
34a7d8
00a990
85acd3
886aae

Requirements
Must have
• The letterhead must have the text in the "contact info" jpg uploaded with the brief.
Nice to have
• We'd like to see some simple, innovating, fresh ideas. A watermark or something interesting in the background would be good.

```html
<!DOCTYPE html>
<html lang="en">
<head>
<meta charset="utf-8">
<title>Marwick Legal – Letterhead</title>
<link rel="stylesheet" href="https://fonts.googleapis.com/css2?family=Poppins:wght@300;400;500&family=Arimo&display=swap">
<style>
  :root {
    --backdrop: #e4e5e7;
    --paper: #f4f4f5;
    --brand-blue: #1f63ad;
    --brand-sky: #5cb6dc;
    --ink: #2a2a2a;
    --ink-dark: #111111;
  }
  * { box-sizing: border-box; margin: 0; padding: 0; }
  html, body {
    width: 1200px; height: 795px; overflow: hidden;
    background: var(--backdrop);
  }
  .letterhead {
    position: absolute;
    left: 338px; top: 27px;
    width: 524px; height: 741px;
    background: var(--paper);
    box-shadow: 0 2px 10px rgba(0,0,0,0.08);
    font-family: 'Poppins', sans-serif;
    color: var(--ink);
  }
  .brand-name {
    position: absolute;
    right: 34px; top: 40px;
    font-weight: 300;
    font-size: 28px;
    letter-spacing: 0.5px;
    color: var(--brand-blue);
  }
  .salutation {
    position: absolute;
    left: 214px; top: 132px;
    font-family: 'Arimo', sans-serif;
    font-size: 9px;
    color: var(--ink-dark);
  }
  .column-rule {
    position: absolute;
    left: 200px; top: 146px;
    width: 1px; height: 530px;
    background: var(--brand-blue);
  }
  .contact-block {
    position: absolute;
    left: 30px; top: 452px;
    width: 160px;
    font-size: 7.6px;
    line-height: 1.45;
  }
  .contact-block .firm-name {
    color: var(--brand-blue);
    font-weight: 500;
    font-size: 8.2px;
    padding-bottom: 5px;
    border-bottom: 1px solid var(--brand-blue);
    width: 118px;
    margin-bottom: 8px;
  }
  .contact-list {
    display: grid;
    grid-template-columns: 54px 1fr;
    row-gap: 0;
  }
  .contact-list dt {
    color: var(--brand-blue);
    font-weight: 500;
  }
  .contact-list dd { color: var(--ink); }
  .contact-list .gap { margin-top: 7px; }
  .legal-note {
    margin-top: 9px;
    padding-top: 7px;
    border-top: 1px solid var(--brand-blue);
    width: 150px;
    font-size: 7.2px;
    line-height: 1.4;
  }
  .bottom-band {
    position: absolute;
    left: 0; right: 0; bottom: 0;
    height: 5px;
    display: flex;
  }
  .bottom-band .band-blue {
    flex: 0 0 56%;
    background: linear-gradient(90deg, var(--brand-sky), var(--brand-blue));
  }
  .bottom-band .band-dark {
    flex: 1;
    background: var(--ink-dark);
  }
</style>
</head>
<body>
  <main class="letterhead">
    <div class="brand-name">Marwick Legal</div>

    <p class="salutation">Dear Sir/Madam</p>
    <div class="column-rule"></div>

    <section class="contact-block">
      <div class="firm-name">MARWICK LEGAL PTY LTD</div>
      <dl class="contact-list">
        <dt>Address:</dt>
        <dd>18 Harbourview Lane<br>Avoca NSW 2251</dd>
        <dt class="gap">All Mail To:</dt>
        <dd class="gap">PO Box 42, Avoca 2251</dd>
        <dt>Tel:</dt>
        <dd>02 4300 1234</dd>
        <dt>Mobile:</dt>
        <dd>0400 555 018</dd>
        <dt>Fax:</dt>
        <dd>02 9000 4471</dd>
        <dt>Email:</dt>
        <dd>jane@marwicklegal.com.au</dd>
        <dt>ABN:</dt>
        <dd>12 345 678 901</dd>
      </dl>
      <p class="legal-note">Liability limited by a scheme approved under Professional Standards Legislation.</p>
      <p class="legal-note">An incorporated legal practice under the Legal Profession Act 2004 as amended</p>
    </section>

    <div class="bottom-band">
      <span class="band-blue"></span>
      <span class="band-dark"></span>
    </div>
  </main>
</body>
</html>
```